Container Web Design Project

I need the front page of my website to have a new, fresh look.
Our company is a highly specialized marketplace for shipping containers (yes, the 20' and 40' kind). Basically, think of Lokko for shipping containers.
I have all of the links/content that I need plugged into a wireframe (attached), and the core color (blue #0073a2) of our existing site should stay the same as we've got stationary, business cards, marketing materials...
If you have any questions please ask.

```html
<!DOCTYPE html>
<html lang="en">
<head>
<meta charset="utf-8">
<title>BoxMarket – Listings</title>
<link href="https://fonts.googleapis.com/css2?family=PT+Sans+Narrow:wght@400;700&display=swap" rel="stylesheet">
<style>
:root{
  --page-bg:#045073;
  --sheet:#ffffff;
  --line:#d4d4d4;
  --panel-line:#cfcfcf;
  --brand:#0073a2;
  --ink:#444444;
  --ink-soft:#555555;
  --footer-ink:#ffffff;
}
*{box-sizing:border-box;margin:0;padding:0}
html,body{width:1200px;height:671px;overflow:hidden}
body{background:var(--page-bg);font-family:Arial,Helvetica,sans-serif;position:relative;color:var(--ink)}
.sheet{position:absolute;left:229px;top:0;width:742px;height:433px;background:var(--sheet);border-radius:0 0 8px 8px}
.sidebar{position:absolute;left:229px;top:0;width:200px;height:433px;border-right:1px solid #e6e6e6;box-shadow:inset -6px 0 8px -6px #e0e0e0}
.sponsor{position:absolute;left:240px;width:176px;height:77px;border:1px solid #cfcfcf;background:#fff;display:flex;align-items:center;justify-content:center;gap:8px;font-family:"PT Sans Narrow",sans-serif;font-weight:700;font-size:24px}
.sponsor--one{top:4px;color:#1d4f91}
.sponsor--two{top:88px;color:#2a9d3c}
.sponsor .mark{width:18px;height:18px;background:currentColor}
.listing-panel{position:absolute;left:439px;top:-10px;width:523px;height:433px;border:1px solid var(--panel-line);border-radius:0 0 6px 6px;background:#fff;overflow:hidden}
.listing{position:absolute;left:8px;width:509px;height:102px;border-bottom:1px solid var(--line)}
.listing__photo{position:absolute;left:0;top:0;width:134px;height:89px;border:1px solid #cfcfcf;border-radius:2px;background:#fff}
.cell{position:absolute;top:0;height:92px;text-align:center}
.cell+.cell{border-left:1px solid #ececec}
.cell--name{left:142px;width:130px}
.cell--type{left:272px;width:81px}
.cell--loc{left:353px;width:73px}
.cell--price{left:426px;width:83px}
.cell__label{position:absolute;top:3px;left:0;right:0;font-size:11px;color:var(--ink)}
.cell__name{position:absolute;top:30px;left:0;right:0;font-family:"PT Sans Narrow",sans-serif;font-weight:700;font-size:16px;line-height:17px;color:var(--brand)}
.cell__size{position:absolute;top:26px;left:0;right:0;font-family:"PT Sans Narrow",sans-serif;font-weight:700;font-size:28px;color:var(--ink-soft)}
.cell__kind{position:absolute;top:56px;left:0;right:0;font-family:"PT Sans Narrow",sans-serif;font-weight:700;font-size:12px;color:var(--ink-soft)}
.cell__loc{position:absolute;top:24px;left:0;right:0;font-family:"PT Sans Narrow",sans-serif;font-weight:700;font-size:12px;line-height:17px;color:var(--ink-soft)}
.cell__price{position:absolute;top:31px;left:0;right:0;font-family:"PT Sans Narrow",sans-serif;font-weight:700;font-size:24px;color:var(--ink-soft)}
.pager{position:absolute;left:439px;top:396px;width:523px;height:20px;font-size:9px;color:var(--ink)}
.pager__prev{position:absolute;left:66px;top:4px}
.pager__next{position:absolute;left:430px;top:4px}
.pager__pages{position:absolute;left:195px;top:1px;display:flex;gap:8px}
.pager__page{width:15px;height:15px;border:1px solid #bdbdbd;font-size:9px;line-height:13px;text-align:center;background:#fff}
.pager__page--current{background:var(--brand);border-color:var(--brand);color:#fff}
.tri{display:inline-block;width:0;height:0;border-top:3px solid transparent;border-bottom:3px solid transparent;vertical-align:1px}
.tri--left{border-right:4px solid var(--ink);margin-right:7px}
.tri--right{border-left:4px solid var(--ink);margin-left:7px}
.legal{position:absolute;left:240px;top:445px;width:720px;text-align:center;font-size:10.5px;line-height:17px;color:var(--footer-ink)}
.footer-links{position:absolute;top:508px;list-style:none;font-size:10.5px;color:var(--footer-ink)}
.footer-links li{height:22px;line-height:15px}
.footer-links li::before{content:"";display:inline-block;border-top:3px solid transparent;border-bottom:3px solid transparent;border-left:4px solid #fff;margin-right:7px;vertical-align:0}
</style>
</head>
<body>
<div class="sheet"></div>
<aside class="sidebar"></aside>
<div class="sponsor sponsor--one"><span class="mark"></span>Northwell Bank</div>
<div class="sponsor sponsor--two">Kindred Fund</div>

<section class="listing-panel">
  <article class="listing" style="top:-6px">
    <div class="listing__photo" role="img" aria-label="Container photo"></div>
    <div class="cell cell--name"><div class="cell__label">Listing Name</div><div class="cell__name">40' New One Trip<br>Door on Both Ends</div></div>
    <div class="cell cell--type"><div class="cell__label">Container Type</div><div class="cell__size">40'</div><div class="cell__kind">Dry box</div></div>
    <div class="cell cell--loc"><div class="cell__label">Location</div><div class="cell__loc">Port Vale /<br>CA, 90811,<br>United States</div></div>
    <div class="cell cell--price"><div class="cell__label">Price</div><div class="cell__price">$5140</div></div>
  </article>
  <article class="listing" style="top:96px">
    <div class="listing__photo" role="img" aria-label="Container photo"></div>
    <div class="cell cell--name"><div class="cell__label">Listing Name</div><div class="cell__name">40' New One Trip<br>Door on Both Ends</div></div>
    <div class="cell cell--type"><div class="cell__label">Container Type</div><div class="cell__size">40'</div><div class="cell__kind">Dry box</div></div>
    <div class="cell cell--loc"><div class="cell__label">Location</div><div class="cell__loc">Port Vale /<br>CA, 90811,<br>United States</div></div>
    <div class="cell cell--price"><div class="cell__label">Price</div><div class="cell__price">$5140</div></div>
  </article>
  <article class="listing" style="top:198px">
    <div class="listing__photo" role="img" aria-label="Container photo"></div>
    <div class="cell cell--name"><div class="cell__label">Listing Name</div><div class="cell__name">40' New One Trip<br>Door on Both Ends</div></div>
    <div class="cell cell--type"><div class="cell__label">Container Type</div><div class="cell__size">40'</div><div class="cell__kind">Dry box</div></div>
    <div class="cell cell--loc"><div class="cell__label">Location</div><div class="cell__loc">Port Vale /<br>CA, 90811,<br>United States</div></div>
    <div class="cell cell--price"><div class="cell__label">Price</div><div class="cell__price">$5140</div></div>
  </article>
  <article class="listing" style="top:300px">
    <div class="listing__photo" role="img" aria-label="Container photo"></div>
    <div class="cell cell--name"><div class="cell__label">Listing Name</div><div class="cell__name">40' New One Trip<br>Door on Both Ends</div></div>
    <div class="cell cell--type"><div class="cell__label">Container Type</div><div class="cell__size">40'</div><div class="cell__kind">Dry box</div></div>
    <div class="cell cell--loc"><div class="cell__label">Location</div><div class="cell__loc">Port Vale /<br>CA, 90811,<br>United States</div></div>
    <div class="cell cell--price"><div class="cell__label">Price</div><div class="cell__price">$5140</div></div>
  </article>
</section>

<nav class="pager">
  <span class="pager__prev"><span class="tri tri--left"></span>PREVIOUS</span>
  <div class="pager__pages">
    <span class="pager__page">1</span><span class="pager__page">2</span><span class="pager__page pager__page--current">3</span><span class="pager__page">4</span><span class="pager__page">5</span><span class="pager__page">···</span><span class="pager__page">25</span>
  </div>
  <span class="pager__next">NEXT<span class="tri tri--right"></span></span>
</nav>

<p class="legal">Copyright © 2011-2013 BoxMarket, Inc. All Rights Reserved. BoxMarket.com is a trademark of BoxMarket Inc. Designated trademarks and brands are the<br>property of their respective owners. Use of this Web site constitutes acceptance of the BoxMarket user agreement and privacy policy.</p>

<ul class="footer-links" style="left:267px"><li>Privacy Policy</li><li>User Agreement</li><li>Help</li></ul>
<ul class="footer-links" style="left:444px"><li>About BoxMarket.com</li><li>News and Articles</li><li>Contact Information</li></ul>
<ul class="footer-links" style="left:631px"><li>Container Dimensions and Weights</li><li>Glossary</li></ul>
<ul class="footer-links" style="left:819px"><li>Browse Locations</li></ul>
</body>
</html>
```